Harlune Painting

Need business card design

Target Market(s)

Paint

Industry/Entity Type

Painting

Requirements
Must have
• Brice Halvorn | Superviser
| HarLune Painting
| mobile: (360) 555-0148
| email: Brice@harluneinc.example
| site: www.harluneinc.example
| address: 718 Corliss Rd NE Ste 300, Olympia, WA 98501

```html
<!DOCTYPE html>
<html lang="en">
<head>
<meta charset="utf-8">
<title>Harlune Painting – Business Cards</title>
<link rel="stylesheet" href="https://fonts.googleapis.com/css2?family=Tinos:wght@700&family=Arimo:wght@400&display=swap">
<style>
  :root {
    --backdrop: #2a2422;
    --card-back: #0a0a0a;
    --card-front: #1c1c1c;
    --brand-blue: #1f3f8e;
    --brand-green: #5cc21f;
    --text-light: #e6e6e6;
    --rule: #9a9a9a;
  }
  * { box-sizing: border-box; margin: 0; padding: 0; }
  html, body { width: 1200px; height: 842px; overflow: hidden; }
  body {
    background: var(--backdrop);
    position: relative;
    font-family: "Arimo", Arial, sans-serif;
  }
  .card {
    position: absolute;
    top: 266px;
    width: 540px;
    height: 310px;
    box-shadow: 0 12px 30px rgba(0,0,0,.55);
    overflow: hidden;
  }
  .card--contact { left: 40px; background: var(--card-back); }
  .card--brand { left: 620px; background: var(--card-front); }

  .band { position: absolute; left: 0; width: 100%; height: 14px; background: var(--brand-blue); }
  .band--top { top: 0; }
  .band--bottom { bottom: 0; }

  .contact-block {
    position: absolute;
    left: 130px;
    top: 74px;
    width: 280px;
    text-align: center;
    color: var(--text-light);
  }
  .holder-name {
    font-family: "Tinos", "Times New Roman", serif;
    font-weight: 700;
    font-size: 19px;
    color: var(--brand-green);
    letter-spacing: .5px;
    text-transform: uppercase;
  }
  .holder-title { font-size: 13px; margin-top: 1px; }
  .divider { height: 1px; background: var(--rule); width: 170px; margin: 10px auto; }
  .contact-list {
    list-style: none;
    display: inline-block;
    font-size: 13px;
    line-height: 17px;
    text-align: left;
  }
  .contact-list .label { color: var(--brand-green); }
  .address { font-size: 13px; line-height: 17px; }

  .tab { position: absolute; background: var(--brand-blue); }
  .tab--left { left: 0; top: 140px; width: 44px; height: 40px; border-right: 3px solid var(--brand-green); }
  .tab--right { right: 0; top: 40px; width: 44px; height: 40px; border-left: 3px solid var(--brand-green); }

  .brand-mark {
    position: absolute;
    left: 0; right: 0;
    top: 135px;
    display: flex;
    justify-content: center;
    align-items: center;
    gap: 12px;
  }
  .brand-square { width: 18px; height: 18px; background: var(--brand-green); }
  .brand-name {
    font-family: "Tinos", "Times New Roman", serif;
    font-weight: 700;
    font-size: 30px;
    color: var(--brand-green);
    text-transform: uppercase;
    letter-spacing: 1px;
  }
</style>
</head>
<body>
  <section class="card card--contact">
    <div class="band band--top"></div>
    <div class="contact-block">
      <p class="holder-name">Brice Halvorn</p>
      <p class="holder-title">Supervisor</p>
      <div class="divider"></div>
      <ul class="contact-list">
        <li><span class="label">M:</span> (360) 555-0148</li>
        <li><span class="label">E:</span> Brice@harluneinc.example</li>
        <li><span class="label">W:</span> www.harluneinc.example</li>
      </ul>
      <div class="divider"></div>
      <p class="address">718 Corliss Rd NE Ste 300<br>Olympia, WA 98501</p>
    </div>
    <div class="band band--bottom"></div>
  </section>

  <section class="card card--brand">
    <div class="tab tab--right"></div>
    <div class="tab tab--left"></div>
    <div class="brand-mark">
      <span class="brand-square"></span>
      <span class="brand-name">Harlune Painting</span>
    </div>
  </section>
</body>
</html>
```